Design a tri-fold brochure for natural vitamin C business.

We are a whole food supplement business specializing in native plant nutrition. We need a tri-fold brochure designed for our natural wholefood vitamin C product. We have developed this product from the organic wild-harvested Australian Kakadu Plum.

The brand is VO-B, and the slogan is True Nature True Health.

My market is the 30-75-year-old male and female customers concerned with a healthy lifestyle.

I would like to see designs using orange, charcoal, and gold and or the designer's own choice of colors.

This brochure is to be a bespoke upmarket design.

I like the idea of a background image like a watermark. However, please be advised that our distributors may photocopy the brochure in black and white, so I don't want the background image to overpower the text and make it difficult to read.

I will provide;
1. Brochure layout
2. Brochure wording
3. Brochure product images
4. Logo image
5. Color hex codes
6. Images pertaining to my product ingredients
7. You may use the full or crop it if you prefer. Do what you think looks best
8. You may reference the file "image-6 TZ Dawn" for an idea of the colors we have used.

- Hex color codes: charcoal (Hex: #333333) orange (Hex: #FF6600) Matte Gold (Hex: #CBAB58)
- Logo: I have attached the logo png file for you to use. Upon choosing a winner, I will supply the logo as eps or ai files for the designer to apply to the final design. There will be two changes to the logo.
a) Change the color from orange to Matte Gold (Hex: #CBAB58)
b) Remove the woman's head from the logo
- You must supply a finished mock-up of the brochure.
- I require all vector files and source files.

```html
<!DOCTYPE html>
<html lang="en">
<head>
<meta charset="utf-8">
<title>VO-B Tri-fold Brochure – Inside Spread</title>
<link href="https://fonts.googleapis.com/css2?family=Open+Sans:wght@300;400;600;700;800&family=Roboto+Condensed:wght@700&display=swap" rel="stylesheet">
<style>
  :root {
    --berry: #b8323f;
    --berry-dark: #9c2434;
    --gold: #f4a62a;
    --gold-soft: #f7b84a;
    --charcoal: #333333;
    --paper: #efefef;
    --paper-shade: #e2e2e2;
    --white: #ffffff;
  }
  * { box-sizing: border-box; margin: 0; padding: 0; }
  html, body { width: 1200px; height: 800px; overflow: hidden; }
  body { background: #4a4a4a; font-family: "Open Sans", Arial, sans-serif; color: var(--charcoal); }
  .spread { display: flex; width: 1200px; height: 800px; }
  .panel { position: relative; width: 400px; height: 800px; padding: 40px 34px; overflow: hidden; }
  .panel--light { background: radial-gradient(circle at 30% 20%, #f8f8f8, var(--paper) 55%, var(--paper-shade)); }
  .leaf-texture { position: absolute; inset: 0; background:
      radial-gradient(ellipse 160px 60px at 80% 30%, rgba(0,0,0,.04), transparent 70%),
      radial-gradient(ellipse 180px 70px at 20% 75%, rgba(0,0,0,.04), transparent 70%); }
  .panel > *:not(.leaf-texture) { position: relative; }

  .kicker { font-weight: 300; font-size: 22px; line-height: 1.1; color: var(--charcoal); }
  .headline { font-weight: 800; font-size: 27px; line-height: 1.1; color: var(--berry); text-transform: uppercase; }
  .rule { height: 2px; background: var(--gold); width: 82%; margin: 8px 0 12px; }
  .body-copy { font-size: 12.5px; line-height: 1.5; }

  .chart-card { margin-top: 16px; background: var(--white); border: 1px solid #cfe0b8; padding: 10px 12px 8px; height: 240px; }
  .chart-card svg { display: block; }

  .quiz { margin-top: 26px; }
  .quiz__box { display: flex; align-items: stretch; background: var(--white); height: 64px; }
  .quiz__mark { width: 58px; background: #e8e8e8; color: var(--gold); font-family: "Roboto Condensed", sans-serif; font-size: 44px; display: flex; align-items: center; justify-content: center; }
  .quiz__question { padding: 8px 12px; font-family: "Roboto Condensed", sans-serif; font-size: 14px; line-height: 1.15; color: var(--charcoal); }
  .quiz__answer { background: var(--berry); color: var(--white); font-weight: 700; font-size: 14px; padding: 7px 14px; }

  .source { margin-top: 38px; }
  .source .kicker { font-weight: 400; font-size: 21px; }

  .panel--berry { display: flex; flex-direction: column; background: linear-gradient(170deg, var(--berry) 0%, var(--berry-dark) 100%); color: var(--white); padding: 22px 34px 24px; }
  .photo-frame { flex: 0 0 236px; background: var(--white); padding: 7px; }
  .photo { width: 100%; height: 100%; background: radial-gradient(circle at 50% 50%, #9aa84a 0%, #6e5a3e 40%, #3b2b22 100%); }
  .panel--berry .headline { color: var(--white); margin-top: 18px; font-size: 24px; }
  .panel--berry .rule { margin: 6px 0 10px; }
  .panel--berry .body-copy { font-size: 11.5px; line-height: 1.42; margin-bottom: 8px; }
  .site-pill { margin-top: auto; flex: 0 0 38px; border-radius: 8px; background: linear-gradient(90deg, var(--gold-soft), var(--gold)); color: var(--white); font-size: 18px; display: flex; align-items: center; justify-content: center; }
  .site-pill b { font-weight: 800; }

  .promise-title { font-weight: 400; font-size: 24px; color: var(--charcoal); }
  .promise-title b { font-weight: 800; color: var(--berry); }
  .promise-list { list-style: none; margin-top: 6px; }
  .promise-item { display: flex; gap: 12px; align-items: center; margin-bottom: 10px; }
  .promise-item svg { flex: 0 0 50px; }
  .promise-item p { font-size: 11.5px; line-height: 1.4; }
  .promise-item strong { color: var(--berry); font-weight: 700; }

  .slogan { margin-top: 12px; font-weight: 400; font-size: 24px; line-height: 1.1; text-transform: uppercase; }
  .slogan b { color: var(--berry); font-weight: 800; }
  .benefits { list-style: none; margin-top: 8px; }
  .benefits li { display: flex; gap: 8px; font-size: 12px; line-height: 1.35; margin-bottom: 2px; }
  .benefits svg { flex: 0 0 12px; margin-top: 3px; }
</style>
</head>
<body>
<main class="spread">

  <section class="panel panel--light">
    <div class="leaf-texture" role="img" aria-label="Faint watermark of Kakadu plum leaves"></div>
    <p class="kicker">Wild-Harvested</p>
    <h2 class="headline">Kakadu Plum</h2>
    <div class="rule"></div>
    <p class="body-copy">Imagine a fruit-based supplement more powerful than any other – one that can protect your health, boost your immune system, reduce your risk of disease and help your body fight dangerous free radicals.</p>

    <figure class="chart-card">
      <svg width="306" height="220" viewBox="0 0 306 220" font-family="Open Sans, sans-serif">
        <defs>
          <linearGradient id="barGold" x1="0" x2="1">
            <stop offset="0" stop-color="#c98f00"/><stop offset=".45" stop-color="#ffd84a"/><stop offset="1" stop-color="#c98f00"/>
          </linearGradient>
        </defs>
        <text x="153" y="10" font-size="7" text-anchor="middle" fill="#333">KPX-100 - Vitamin C Milligrams/100g (Dry Weight)</text>
        <g stroke="#ddd" stroke-width="1">
          <line x1="20" y1="30" x2="280" y2="30"/><line x1="20" y1="62" x2="280" y2="62"/>
          <line x1="20" y1="94" x2="280" y2="94"/><line x1="20" y1="126" x2="280" y2="126"/>
          <line x1="20" y1="158" x2="280" y2="158"/><line x1="20" y1="190" x2="280" y2="190"/>
        </g>
        <g font-size="6" fill="#333">
          <text x="284" y="32">25,000</text><text x="284" y="64">20,000</text><text x="284" y="96">15,000</text>
          <text x="284" y="128">10,000</text><text x="284" y="160">5,000</text><text x="284" y="192">0</text>
        </g>
        <g fill="url(#barGold)">
          <rect x="28" y="189" width="30" height="1"/><rect x="70" y="189" width="30" height="1"/>
          <rect x="112" y="168" width="30" height="22"/><rect x="154" y="159" width="30" height="31"/>
          <rect x="196" y="144" width="30" height="46"/><rect x="238" y="62" width="30" height="128"/>
        </g>
        <g font-size="6.5" fill="#333" text-anchor="middle">
          <text x="43" y="184">65</text><text x="85" y="184">110</text><text x="127" y="163">3,445</text>
          <text x="169" y="154">4,800</text><text x="211" y="139">7,253</text><text x="253" y="57">20,000</text>
        </g>
        <g font-size="5.5" fill="#333" text-anchor="middle">
          <text x="43" y="201">Blueberry</text><text x="85" y="201">Orange</text><text x="127" y="201">Acerola Cherry</text>
          <text x="169" y="201">Camu Camu</text><text x="211" y="201">Kakadu Plum (Std)</text><text x="253" y="210">Kakadu Plum (KPX-100)</text>
        </g>
      </svg>
    </figure>

    <div class="quiz">
      <div class="quiz__box">
        <div class="quiz__mark">Q</div>
        <p class="quiz__question">How many peeled oranges does one need to consume to reach 20,000mg of vitamin C?</p>
      </div>
      <p class="quiz__answer">Approximately *377 (37,736g / 37.73kg)</p>
    </div>

    <div class="source">
      <p class="kicker">Nature’s Richest Source</p>
      <h2 class="headline">Of Vitamin C</h2>
      <div class="rule"></div>
      <p class="body-copy">Wild-harvested Kakadu plum (Terminalia ferdinandiana) is nature’s most potent source of vitamin C. It’s one of the world’s few true superfoods.</p>
    </div>
  </section>

  <section class="panel panel--berry">
    <div class="photo-frame">
      <div class="photo" role="img" aria-label="Photograph of cupped hands holding freshly picked green Kakadu plums"></div>
    </div>
    <h2 class="headline">Organic. Fair Trade. Sustainable.</h2>
    <div class="rule"></div>
    <p class="body-copy">The Kakadu plum has been a part of traditional Aboriginal medicine for more than 40,000 years. Ancient cultural wisdom paved the way for this wild-grown Australian superfood’s modern use as an antioxidant, anti-inflammatory and antimicrobial agent.</p>
    <p class="body-copy">Harvested in the pristine outback wilderness by Australia’s indigenous people and certified by Aboriginal elders, wild-picked Kakadu plum grows without modern or commercial farming techniques. No pesticides, synthetic fertilizers or GMOs – just as nature intended.</p>
    <p class="body-copy">The income from wild-harvested Kakadu plum directly supports local indigenous communities. Because these superfruits are selectively hand-picked by people who have lived on and respected the land for centuries, they’re sustainably and responsibly harvested – and these caretakers ensure that the land and its bounty are preserved for future generations.</p>
    <p class="site-pill">www.<b>vo-b</b>.club</p>
  </section>

  <section class="panel panel--light">
    <div class="leaf-texture" role="img" aria-label="Faint watermark of Kakadu plum leaves"></div>
    <h2 class="promise-title">THE <b>VO-B PROMISE</b></h2>
    <div class="rule"></div>
    <ul class="promise-list">
      <li class="promise-item">
        <svg width="50" height="50" viewBox="0 0 50 50"><circle cx="25" cy="25" r="23" fill="#b8323f" stroke="#f4a62a" stroke-width="2"/><path d="M15 30 q10 6 20 0 M25 14 q8 4 0 14 q-8 -10 0 -14" fill="none" stroke="#fff" stroke-width="2"/></svg>
        <p><strong>100% natural.</strong> Our vitamin C is – and always will be – sourced from natural, organic and wild-harvested whole foods.</p>
      </li>
      <li class="promise-item">
        <svg width="50" height="50" viewBox="0 0 50 50"><circle cx="25" cy="25" r="23" fill="#b8323f" stroke="#f4a62a" stroke-width="2"/><path d="M17 35 L33 15 M22 28 l-5 -2 M26 23 l-5 -2 M30 18 l-5 -2 M22 28 l2 -5 M26 23 l2 -5 M30 18 l2 -5" fill="none" stroke="#fff" stroke-width="2"/></svg>
        <p><strong>100% ethical.</strong> We sustainably source all ingredients in our supplements through fair trade practices.</p>
      </li>
      <li class="promise-item">
        <svg width="50" height="50" viewBox="0 0 50 50"><circle cx="25" cy="25" r="23" fill="#b8323f" stroke="#f4a62a" stroke-width="2"/><circle cx="25" cy="22" r="8" fill="none" stroke="#fff" stroke-width="2"/><path d="M21 24 q4 3 8 0 M14 32 q11 8 22 0" fill="none" stroke="#fff" stroke-width="2"/></svg>
        <p><strong>100% transparent.</strong> We share every ingredient in every product; you always know what you’re getting.</p>
      </li>
      <li class="promise-item">
        <svg width="50" height="50" viewBox="0 0 50 50"><circle cx="25" cy="25" r="23" fill="#b8323f" stroke="#f4a62a" stroke-width="2"/><circle cx="25" cy="25" r="11" fill="none" stroke="#fff" stroke-width="2"/><line x1="15" y1="35" x2="35" y2="15" stroke="#fff" stroke-width="2"/></svg>
        <p><strong>0% synthetics.</strong> We never use synthetic ingredients, fillers or stabilizers. Our products are completely natural.</p>
      </li>
    </ul>

    <h2 class="slogan">True <b>Nature,</b><br>True <b>Health</b></h2>
    <div class="rule"></div>
    <p class="body-copy" style="font-size:12px">Pure, natural whole foods are the most effective way to maintain physical and mental health – and vitamin C from wild-harvested Kakadu plum is a powerful example of nature’s capabilities. Vitamin C may:</p>
    <ul class="benefits">
      <li><svg width="12" height="12" viewBox="0 0 12 12"><circle cx="6" cy="6" r="5" fill="none" stroke="#b8323f"/><path d="M3.5 6 l2 2 l3 -4" fill="none" stroke="#b8323f"/></svg>Help you manage blood pressure</li>
      <li><svg width="12" height="12" viewBox="0 0 12 12"><circle cx="6" cy="6" r="5" fill="none" stroke="#b8323f"/><path d="M3.5 6 l2 2 l3 -4" fill="none" stroke="#b8323f"/></svg>Lower your risk of chronic disease</li>
      <li><svg width="12" height="12" viewBox="0 0 12 12"><circle cx="6" cy="6" r="5" fill="none" stroke="#b8323f"/><path d="M3.5 6 l2 2 l3 -4" fill="none" stroke="#b8323f"/></svg>Help control metabolism</li>
      <li><svg width="12" height="12" viewBox="0 0 12 12"><circle cx="6" cy="6" r="5" fill="none" stroke="#b8323f"/><path d="M3.5 6 l2 2 l3 -4" fill="none" stroke="#b8323f"/></svg>Prevent iron deficiency</li>
      <li><svg width="12" height="12" viewBox="0 0 12 12"><circle cx="6" cy="6" r="5" fill="none" stroke="#b8323f"/><path d="M3.5 6 l2 2 l3 -4" fill="none" stroke="#b8323f"/></svg>Boost your immunity</li>
      <li><svg width="12" height="12" viewBox="0 0 12 12"><circle cx="6" cy="6" r="5" fill="none" stroke="#b8323f"/><path d="M3.5 6 l2 2 l3 -4" fill="none" stroke="#b8323f"/></svg>Protect your memory as you age</li>
      <li><svg width="12" height="12" viewBox="0 0 12 12"><circle cx="6" cy="6" r="5" fill="none" stroke="#b8323f"/><path d="M3.5 6 l2 2 l3 -4" fill="none" stroke="#b8323f"/></svg>Improve nervous system function</li>
      <li><svg width="12" height="12" viewBox="0 0 12 12"><circle cx="6" cy="6" r="5" fill="none" stroke="#b8323f"/><path d="M3.5 6 l2 2 l3 -4" fill="none" stroke="#b8323f"/></svg>Serve as an essential cofactor for many enzymes in the body</li>
      <li><svg width="12" height="12" viewBox="0 0 12 12"><circle cx="6" cy="6" r="5" fill="none" stroke="#b8323f"/><path d="M3.5 6 l2 2 l3 -4" fill="none" stroke="#b8323f"/></svg>Support collagen synthesis</li>
      <li><svg width="12" height="12" viewBox="0 0 12 12"><circle cx="6" cy="6" r="5" fill="none" stroke="#b8323f"/><path d="M3.5 6 l2 2 l3 -4" fill="none" stroke="#b8323f"/></svg>Play a role in connective tissue healing</li>
      <li><svg width="12" height="12" viewBox="0 0 12 12"><circle cx="6" cy="6" r="5" fill="none" stroke="#b8323f"/><path d="M3.5 6 l2 2 l3 -4" fill="none" stroke="#b8323f"/></svg>Help regenerate vitamin E in the body</li>
      <li><svg width="12" height="12" viewBox="0 0 12 12"><circle cx="6" cy="6" r="5" fill="none" stroke="#b8323f"/><path d="M3.5 6 l2 2 l3 -4" fill="none" stroke="#b8323f"/></svg>Assist in producing the potent free-radical protector, glutathione</li>
    </ul>
  </section>

</main>
</body>
</html>
```